Artist/Artwork Product Catalog

I need a small brief product catalog to display my art for purchase to my interior designer clients, to purchase for their clients. Should be 5 - 10 pages with art/canvas display mock up pictures. Sections should include About the artist, space for pricing and art titles, Editable Section Names (3 sections-not including previously mentioned sections), Contact info-including social media. I would like modern and simplistic. My art is filled with bright colors and as such want the design of the catalog to be black and white so as not to detract from the art itself. Please refer to my website and instagram for further design resource: www.teroquillbay.com ; @quillbayteros (instagram)
Target Market(s)
Interior Designers, Collectors, Galleries
Industry/Entity Type
Art Gallery
Colors
Designer to choose colors to be used in the design.
Requirements
Must have
- Must have my artwork included in catalog displayed in canvas wall art mock up. Will send files upon acceptance of catalog design. Need to be printer ready upon project completion as well as editable for future changes as needed. Would like a smaller sized catalog, maybe A4.
Nice to have
- Editable for future use. Would love to have new logo integrated into catalog.
Should not have
- No distracting colors or ornate decorative design

```html
<!DOCTYPE html>
<html lang="en">
<head>
<meta charset="utf-8">
<title>Bloom — Art Catalogue Page</title>
<link rel="stylesheet" href="https://fonts.googleapis.com/css2?family=Open+Sans:wght@300;400&display=swap">
<style>
  :root {
    --backdrop: #ffffff;
    --page: #231f20;
    --ink: #ffffff;
    --ink-soft: #e6e6e6;
    --accent: #e41fd2;
    --frame: #f2f2f2;
  }
  html, body {
    margin: 0;
    width: 1200px;
    height: 1200px;
    overflow: hidden;
    background: var(--backdrop);
  }
  .catalogue-page {
    position: absolute;
    left: 151px;
    top: 41px;
    width: 898px;
    height: 1118px;
    background: var(--page);
    font-family: "Open Sans", sans-serif;
    color: var(--ink);
  }
  .intro-text {
    position: absolute;
    left: 37px;
    top: 41px;
    width: 66px;
    height: 693px;
    margin: 0;
    writing-mode: vertical-rl;
    transform: rotate(180deg);
    font-size: 11.4px;
    line-height: 13px;
    color: var(--ink-soft);
    text-align: left;
  }
  .collection-name {
    position: absolute;
    left: 44px;
    top: 880px;
    margin: 0;
    writing-mode: vertical-rl;
    transform: rotate(180deg);
    font-weight: 300;
    font-size: 62px;
    line-height: 62px;
    letter-spacing: 1px;
    color: var(--accent);
    height: 210px;
  }
  .divider {
    position: absolute;
    left: 132px;
    top: 30px;
    width: 3px;
    height: 1056px;
    background: var(--accent);
  }
  .artwork {
    position: absolute;
    left: 162px;
    width: 690px;
    height: 320px;
  }
  .artwork-title {
    position: absolute;
    left: 3px;
    top: 0;
    margin: 0;
    font-weight: 400;
    font-size: 23px;
    line-height: 26px;
  }
  .artwork-frame {
    position: absolute;
    left: 0;
    top: 42px;
    width: 269px;
    height: 269px;
    border: 2px solid var(--frame);
    background: #111;
  }
  .artwork-image {
    position: absolute;
    inset: 11px;
  }
  .bloom-01 .artwork-image { background: radial-gradient(circle, #f4a23b 0%, #f36b2c 40%, #4a3fd8 75%, #e9f3ea 100%); }
  .bloom-02 .artwork-image { background: radial-gradient(circle, #f06bd0 0%, #e33fc8 40%, #2ec4b2 75%, #f3efe0 100%); }
  .bloom-03 .artwork-image { background: radial-gradient(circle, #fbc04a 0%, #f3a235 40%, #8a45d8 75%, #eef5ec 100%); }
  .artwork-details {
    position: absolute;
    left: 284px;
    top: 45px;
    width: 400px;
    font-size: 11.6px;
    line-height: 14.4px;
    color: var(--ink-soft);
  }
  .detail-label {
    margin: 0;
    color: var(--accent);
    font-size: 11.6px;
    font-weight: 400;
  }
  .detail-text {
    margin: 0 0 9px;
  }
  .artwork-price {
    position: absolute;
    right: 9px;
    top: 278px;
    margin: 0;
    font-size: 27px;
    line-height: 30px;
    font-weight: 400;
  }
  .price-label {
    color: var(--accent);
    font-size: 22px;
    font-weight: 300;
  }
</style>
</head>
<body>
<main class="catalogue-page">
  <p class="intro-text">Proin facilisis elit vitae mollis faucibus. Proin vitae massa nec mauris dictum consequat. Maecenas congue non felis a malesuada. Phasellus ullamcorper laoreet felis eu viverra. In at tincidunt tortor. Praesent tempor eros vitae elit dignissim, vitae elementum dui dapibus. Duis tristique, ligula eget lobortis accumsan, nibh enim venenatis urna, a commodo elit ex ac urna.</p>
  <h1 class="collection-name">BLOOM</h1>
  <div class="divider"></div>

  <section class="artwork bloom-01" style="top:41px">
    <h2 class="artwork-title">Title BLOOM 01</h2>
    <div class="artwork-frame"><div class="artwork-image" role="img" aria-label="Artwork: hand-drawn orange four-petal flower on blue scrolls, square tile"></div></div>
    <div class="artwork-details">
      <h3 class="detail-label">ABOUT ART</h3>
      <p class="detail-text">Proin facilisis elit vitae mollis faucibus. Proin vitae massa nec mauris dictum consequat. Maecenas congue non felis a malesuada. Phasellus ullamcorper laoreet felis eu viverra.</p>
      <h3 class="detail-label">ABOUT ARTIST</h3>
      <p class="detail-text">Proin facilisis elit vitae mollis faucibus. Proin vitae massa nec mauris dictum consequat.</p>
      <h3 class="detail-label">Secition 03 and 04</h3>
      <p class="detail-text">Proin facilisis elit vitae mollis faucibus. Proin vitae massa nec mauris dictum consequat. Maecenas congue non felis a malesuada. Phasellus ullamcorper laoreet felis eu viverra.</p>
    </div>
    <p class="artwork-price"><span class="price-label">Price:</span> 650$</p>
  </section>

  <section class="artwork bloom-02" style="top:408px">
    <h2 class="artwork-title">Title BLOOM 02</h2>
    <div class="artwork-frame"><div class="artwork-image" role="img" aria-label="Artwork: hand-drawn pink four-petal flower on teal scrolls, square tile"></div></div>
    <div class="artwork-details">
      <h3 class="detail-label">ABOUT ART</h3>
      <p class="detail-text">Proin facilisis elit vitae mollis faucibus. Proin vitae massa nec mauris dictum consequat. Maecenas congue non felis a malesuada. Phasellus ullamcorper laoreet felis eu viverra.</p>
      <h3 class="detail-label">ABOUT ARTIST</h3>
      <p class="detail-text">Proin facilisis elit vitae mollis faucibus. Proin vitae massa nec mauris dictum consequat.</p>
      <h3 class="detail-label">Secition 03 and 04</h3>
      <p class="detail-text">Proin facilisis elit vitae mollis faucibus. Proin vitae massa nec mauris dictum consequat. Maecenas congue non felis a malesuada. Phasellus ullamcorper laoreet felis eu viverra.</p>
    </div>
    <p class="artwork-price"><span class="price-label">Price:</span> 650$</p>
  </section>

  <section class="artwork bloom-03" style="top:770px">
    <h2 class="artwork-title">Title BLOOM 03</h2>
    <div class="artwork-frame"><div class="artwork-image" role="img" aria-label="Artwork: hand-drawn golden four-petal flower on purple scrolls, square tile"></div></div>
    <div class="artwork-details">
      <h3 class="detail-label">ABOUT ART</h3>
      <p class="detail-text">Proin facilisis elit vitae mollis faucibus. Proin vitae massa nec mauris dictum consequat. Maecenas congue non felis a malesuada. Phasellus ullamcorper laoreet felis eu viverra.</p>
      <h3 class="detail-label">ABOUT ARTIST</h3>
      <p class="detail-text">Proin facilisis elit vitae mollis faucibus. Proin vitae massa nec mauris dictum consequat.</p>
      <h3 class="detail-label">Secition 03 and 04</h3>
      <p class="detail-text">Proin facilisis elit vitae mollis faucibus. Proin vitae massa nec mauris dictum consequat. Maecenas congue non felis a malesuada. Phasellus ullamcorper laoreet felis eu viverra.</p>
    </div>
    <p class="artwork-price"><span class="price-label">Price:</span> 650$</p>
  </section>
</main>
</body>
</html>
```